PPT Template Graphic Design for Firm Serving Sales & Mrkting Executives in High-Tech Comopanies

Brookvane seeks a graphic design for a PowerPoint template for corporate presentations.
We are a workforce solutions company that specializes in finding and managing contractors for sales and marketing organizations in high-tech companies. We can also manage entire processes with our 'managed services' solution, for existing clients. We are unique in our exclusive focus on sales & marketing, our consultative approach that works with clients to leverage contractors, not just to fill immediate resource gaps they may have, but also to achieve immediate and longer term business goals of their organization. We offer the dual advantage of flexibility as clients may find within a boutique firm, and the scalability of a global company which means that regardless of whether clients need one contractor or several, locally or in foreign markets, we can help.
We will use this PPT template to present what we do to help clients, and how we are different from the competition to prospective clients. We might also use this PPT template to present proposals.
Updates

Project Deadline Extended
Reason: We would love to see some more design options! Also, we have guaranteed the project since we first posted. Thank you!

Target Market(s)

Executives in sales and marketing organizations of high tech companies, including VP of Sales, VP marketing, CEO, CFO and heads of HR departments.

Industry/Entity Type

Graphic Design

Requirements
Must have
• Template must be simple, elegant, classy. Please include a cover page, supporting pages (for content of presentation) and concluding ("Thank You") page. Design must include our logo & tagline (see attached), and provide recommendations for heading font, copy font and ‘bullet’ styles. Please locate company name on bottom right of template. Design should be in the same family of the look and feel of our website (www.brookvane-example.com). We would like the design to convey simplicity and elegance. We’d also like it to reflect the personality of our firm: friendly and approachable, with a high level of professionalism. Design should feel confident, and up-to-date in its look. Template must be both MAC and PC compatible.
Nice to have
• Same template developed for PPT, imported into a Prezi format as well. We need the PPT template for sure, but one in Prezi would be great to have as well - to enable more professional looking format for presentations.

```html
<!DOCTYPE html>
<html lang="en">
<head>
<meta charset="utf-8">
<title>Brookvane Presentation Template</title>
<link href="https://fonts.googleapis.com/css2?family=Ubuntu:ital,wght@0,400;0,500;0,700;1,400&family=Open+Sans:wght@400;600;700&display=swap" rel="stylesheet">
<style>
  :root{
    --orange:#f26a21;
    --orange-light:#f7a46f;
    --grey:#6d6e71;
    --grey-dark:#58595b;
    --dot-brown:#b89a8a;
    --paper:#ffffff;
    --canvas:#ffffff;
    --text:#231f20;
  }
  *{box-sizing:border-box;margin:0;padding:0}
  html,body{width:1200px;height:900px;overflow:hidden;background:var(--canvas)}
  body{position:relative;font-family:"Open Sans",Arial,sans-serif;color:var(--text)}

  .slide{position:absolute;width:400px;height:300px;background:var(--paper);
    box-shadow:0 2px 8px rgba(0,0,0,.35);overflow:hidden}
  .slide--cover{left:15px;top:20px;z-index:3}
  .slide--info{left:785px;top:30px;z-index:4}
  .slide--section{left:392px;top:250px;z-index:2}
  .slide--table{left:12px;top:520px;z-index:1}
  .slide--quotes{left:785px;top:575px;z-index:5}

  .dot-column{position:absolute;left:0;top:0;width:48px;height:100%;
    background:linear-gradient(180deg,rgba(184,154,138,.35) 0%,var(--dot-brown) 40%,var(--orange-light) 75%,var(--orange) 100%);
    -webkit-mask:linear-gradient(90deg,#000 0%,rgba(0,0,0,.45) 100%);
    mask:linear-gradient(90deg,#000 0%,rgba(0,0,0,.45) 100%)}

  .illustration{position:absolute;border-radius:6px;
    background:radial-gradient(ellipse at 50% 55%,#e6e6e6 0%,#f3f3f3 55%,#fff 80%)}

  .brand{position:absolute;right:12px;bottom:10px;text-align:left}
  .brand__name{display:flex;align-items:center;gap:5px;font-family:"Ubuntu",sans-serif;
    font-weight:500;color:var(--grey-dark);line-height:1}
  .brand__dot{border-radius:50%;background:var(--grey)}
  .brand__tagline{font-family:"Ubuntu",sans-serif;color:var(--grey);display:block;white-space:nowrap}
  .brand--large .brand__name{font-size:24px}
  .brand--large .brand__dot{width:20px;height:20px}
  .brand--large .brand__tagline{font-size:8.5px;margin-top:3px}
  .brand--small .brand__name{font-size:13px}
  .brand--small .brand__dot{width:11px;height:11px}
  .brand--small .brand__tagline{font-size:5px;margin-top:2px}

  .footer-rule{position:absolute;left:0;right:0;bottom:14px;height:2px;background:var(--orange)}
  .footer-page{position:absolute;left:6px;bottom:3px;font-size:6px;color:var(--grey)}

  /* cover */
  .cover__title{position:absolute;left:115px;top:12px;font-family:"Ubuntu",sans-serif;
    font-weight:500;color:var(--orange);font-size:19px;line-height:1.15;letter-spacing:.5px}
  .cover__title strong{color:var(--grey-dark);font-size:25px;font-weight:500}

  /* info */
  .info__mark{position:absolute;left:14px;top:36px;width:26px;height:26px;border-radius:50%;background:var(--grey)}
  .pill{position:absolute;color:#fff;font-family:"Ubuntu",sans-serif;font-weight:700;letter-spacing:.8px}
  .pill--title{left:0;top:92px;width:190px;height:22px;background:var(--orange);
    border-radius:0 11px 11px 0;font-size:11.5px;padding:4px 0 0 10px}
  .pill--subtitle{left:0;top:118px;width:190px;height:18px;background:var(--orange);
    border-radius:0 9px 9px 0;font-size:5.5px;text-align:right;padding:2px 10px 0 0;line-height:1.2}
  .pill--grey{right:0;top:136px;width:158px;height:18px;background:var(--grey);
    border-radius:9px 0 0 9px;font-size:11px;padding:2px 0 0 10px;font-weight:500}
  .info__rule{position:absolute;left:8px;right:10px;top:164px;height:1px;background:var(--orange-light)}
  .info__col{position:absolute;top:180px;width:180px;font-size:5.3px;line-height:1.35;font-weight:600}
  .info__col p+p{margin-top:5px}
  .info__col--left{left:6px}
  .info__col--right{left:206px}

  /* section */
  .section__tab{position:absolute;right:0;top:66px;width:128px;height:16px;background:var(--orange);
    border-radius:8px 0 0 8px;color:#fff;font-family:"Ubuntu",sans-serif;font-weight:700;
    font-size:11px;text-align:right;padding:1px 8px 0 0;letter-spacing:.5px}
  .section__num{position:absolute;right:10px;top:46px;width:18px;height:18px;border-radius:50%;
    background:var(--grey-dark);color:#fff;font-size:10px;font-weight:700;text-align:center;line-height:18px}
  .section__heading{position:absolute;left:168px;top:88px;font-family:"Ubuntu",sans-serif;
    font-weight:500;color:var(--orange);font-size:25px}
  .section__bullets{position:absolute;left:215px;top:150px;list-style:none;font-family:"Ubuntu",sans-serif;
    font-style:italic;color:var(--grey);font-size:11.5px;line-height:22px}
  .section__bullets li::before{content:"• "}

  /* table */
  .rows{position:absolute;left:178px;top:67px;width:122px;list-style:none}
  .rows li{height:22px;margin-bottom:4px;border-radius:3px;background:linear-gradient(180deg,#f5894a,var(--orange));
    color:#fff;font-size:7px;font-weight:600;text-align:center;line-height:22px;box-shadow:0 1px 2px rgba(0,0,0,.3)}
  .rows li.rows__item--muted{background:linear-gradient(180deg,#7a7b7e,var(--grey-dark))}

  /* quotes */
  .quote{position:absolute;right:12px;width:152px;text-align:right;font-family:"Ubuntu",sans-serif}
  .quote__text{font-size:9.3px;font-weight:500;line-height:1.2;color:var(--text)}
  .quote__by{font-size:6px;color:var(--grey);margin-top:3px;line-height:1.25}
</style>
</head>
<body>

  <section class="slide slide--table" aria-label="Table slide">
    <div class="dot-column" role="img" aria-label="Column of graded dots"></div>
    <div class="illustration" style="left:30px;top:165px;width:110px;height:110px" role="img" aria-label="Illustration of two white figures shaking hands"></div>
    <ul class="rows">
      <li>table type information</li>
      <li>table type information</li>
      <li>table type information</li>
      <li>table type information</li>
      <li>table type information</li>
      <li class="rows__item--muted">table type information</li>
    </ul>
    <div class="footer-rule"></div>
    <span class="footer-page">part C &nbsp; 5</span>
    <div class="brand brand--small" style="bottom:18px">
      <span class="brand__name"><span class="brand__dot"></span>Brookvane</span>
      <span class="brand__tagline">Driving sales growth with people</span>
    </div>
  </section>

  <section class="slide slide--section" aria-label="Section slide">
    <div class="dot-column" role="img" aria-label="Column of graded dots"></div>
    <span class="section__num">1</span>
    <div class="section__tab">part A</div>
    <h2 class="section__heading">Heading</h2>
    <ul class="section__bullets">
      <li>Bullet 1</li><li>Bullet 2</li><li>Bullet 3</li><li>Bullet 4</li>
    </ul>
    <div class="illustration" style="left:0;top:165px;width:130px;height:125px" role="img" aria-label="Illustration of a red figure carrying a large power plug"></div>
  </section>

  <section class="slide slide--cover" aria-label="Cover slide">
    <div class="dot-column" role="img" aria-label="Column of graded dots"></div>
    <h1 class="cover__title">Do <strong>More</strong> than<br>Fill the Gaps</h1>
    <div class="illustration" style="left:120px;top:82px;width:150px;height:150px" role="img" aria-label="Illustration of a white figure with raised arms behind a velvet rope barrier"></div>
    <div class="brand brand--large" style="bottom:22px">
      <span class="brand__name"><span class="brand__dot"></span>Brookvane</span>
      <span class="brand__tagline">Driving sales growth with people</span>
    </div>
    <div class="footer-rule" style="bottom:6px"></div>
  </section>

  <section class="slide slide--info" aria-label="Information slide">
    <span class="info__mark"></span>
    <div class="pill pill--title">IMPORTANT INFORMATION</div>
    <div class="pill pill--subtitle">IMPORTANT INFORMATION<br>ON TWO LINES</div>
    <div class="pill pill--grey">Sub Heading</div>
    <div class="info__rule"></div>
    <div class="info__col info__col--left">
      <p>Lorem ipsum dolor sit amet, pellentesque mauris ligula magna ut. Mauris duis pretium, vitae in ad viverra, dictum placerat. Turpis nunc. Vestibulum est cras, donec in suscipit, vitae ut feugiat. Non maxime, ipsum suspendisse consectetuer. Donec id aliquam nulla arcu, orci inceptos metus molestie lorem quis, sed orci lacus, vestibulum sit. Aenean ut tellus volutpat, orci nec cum justo tortor, convallis lorem nostra ipsum eget. Imperdiet maecenas quis fermentum, eget donec felis mi orci justo aliquet. Lectus viverra donec nunc quam commodo, conubia risus. Vitae sagittis lacus ullamcorper sagittis nec ultricies, elit cursus consequat faucibus nam ac est. Tellus viverra, nostra integer, tellus mollis sint, in commodo eu ultrices, turpis facilisi ut velit.</p>
      <p>Cursus etiam, wisi vitae vitae laoreet, odio non quis congue ut.</p>
    </div>
    <div class="info__col info__col--right">
      <p>Lorem ipsum dolor sit amet, pellentesque mauris ligula magna ut. Mauris duis pretium, vitae in ad viverra, dictum placerat. Turpis nunc. Vestibulum est cras, donec in suscipit, vitae ut feugiat. Non maxime, ipsum suspendisse consectetuer. Donec id aliquam nulla arcu, orci inceptos metus molestie lorem quis, sed orci lacus, vestibulum sit.</p>
      <p>Aenean ut tellus volutpat, orci nec cum justo tortor, convallis lorem nostra ipsum eget. Imperdiet maecenas quis fermentum, eget</p>
    </div>
    <span class="footer-page">part A &nbsp; 3</span>
    <div class="brand brand--small" style="bottom:6px">
      <span class="brand__name"><span class="brand__dot"></span>Brookvane</span>
      <span class="brand__tagline">Driving sales growth with people</span>
    </div>
  </section>

  <section class="slide slide--quotes" aria-label="Testimonials slide">
    <div class="dot-column" role="img" aria-label="Column of graded dots"></div>
    <div class="illustration" style="left:120px;top:70px;width:140px;height:150px" role="img" aria-label="Illustration of white figures climbing a spiral staircase"></div>
    <blockquote class="quote" style="top:8px">
      <p class="quote__text">"The first thing that comes to mind is Brookvane's attention to benefits for its employees. The benefits we receive are quite generous."</p>
      <p class="quote__by">– Dana Whitfield, Marketing and Operations<br>Manager for Latin America</p>
    </blockquote>
    <blockquote class="quote" style="top:100px">
      <p class="quote__text">"The first thing that comes to mind is Brookvane's attention to benefits for its employees. The benefits we receive are quite generous."</p>
      <p class="quote__by">– Dana Whitfield, Marketing and Operations<br>Manager for Latin America</p>
    </blockquote>
    <blockquote class="quote" style="top:192px">
      <p class="quote__text">"The first thing that comes to mind is Brookvane's attention to benefits for its employees. The benefits we receive are quite generous."</p>
      <p class="quote__by">– Dana Whitfield, Marketing and Operations<br>Manager for Latin America</p>
    </blockquote>
    <div class="brand brand--small" style="bottom:4px">
      <span class="brand__name"><span class="brand__dot"></span>Brookvane</span>
      <span class="brand__tagline">Driving sales growth with people</span>
    </div>
  </section>

</body>
</html>
```